Webdesign für Verkauf von Stoffen
Zielgruppe
Palmtuche ist schon seit 15 Jahren auf den Märkten unterwegs und verkauft seine hochwertigen Stoffe vor Ort. Nun muss die Webseite ein neuen Look bekommen, sie sollte modern und locker wirken. Die Webseite ist eher für Privatkunden und hat jetzt noch keine Shop Möglichkeit, die wird aber intrigiert mit einzelnen Produkten.
Aufgabenstellung
Logo gibt es noch nicht, soll erstmal nur in Schriftform bleiben, ansonsten gibt es keine explizierten Vorgaben

```html
<!DOCTYPE html>
<html lang="de">
<head>
<meta charset="utf-8">
<title>Palmtuche – Bunte Bahnen</title>
<link href="https://fonts.googleapis.com/css2?family=Jost:wght@300;400;500;600;700&display=swap" rel="stylesheet">
<style>
:root{
  --navy:#1d2a6e;
  --navy-deep:#0f1c4f;
  --gold:#c49a3c;
  --grey:#e4e4e4;
  --line:#8a90ad;
  --white:#ffffff;
}
*{box-sizing:border-box;margin:0;padding:0}
html,body{width:1200px;height:2250px;overflow:hidden;background:var(--white)}
body{position:relative;font-family:'Jost',sans-serif;color:var(--navy)}
.abs{position:absolute}

/* header */
.site-header{left:0;top:0;width:1200px;height:87px}
.brand{left:40px;top:28px;display:flex;align-items:center;gap:10px}
.brand-mark{width:22px;height:22px;border:2px solid var(--navy)}
.brand-name{font-size:21px;font-weight:400;letter-spacing:.5px;color:var(--navy)}
.main-nav{left:665px;top:37px;display:flex;gap:29px;font-size:9.5px;font-weight:600;letter-spacing:1.6px}
.main-nav .active{position:relative}
.main-nav .active::before{content:"";position:absolute;left:-2px;right:-2px;top:-37px;height:3px;background:var(--gold)}
.nav-divider{left:1106px;top:14px;width:1px;height:54px;background:var(--line)}
.cart{left:1134px;top:24px}

/* hero */
.hero{left:0;top:87px;width:1200px;height:325px;background:linear-gradient(90deg,#3b86b5,#d6483a 18%,#f0b534 32%,#2c5fa8 48%,#e05b3b 62%,#f2c64b 74%,#c93a3c 86%,#3aa0a0)}
.hero-badge{left:264px;top:175px;width:673px;height:136px;background:var(--navy);text-align:center;color:var(--white)}
.stitch{position:absolute;top:6px;bottom:6px;border-left:1px dashed var(--gold)}
.hero-title{font-size:46px;font-weight:400;letter-spacing:1px;margin-top:20px;line-height:1.1}
.hero-tagline{font-size:28px;font-weight:300;color:var(--gold);margin-top:4px}

/* intro */
.intro{left:0;top:455px;width:1200px;text-align:center}
.intro h1{font-size:29px;font-weight:300;letter-spacing:.5px}
.intro .rule{width:76px;height:2px;background:var(--gold);margin:14px auto 18px}
.intro p{font-size:17.5px;font-weight:300;line-height:1.35;width:660px;margin:0 auto}

.category{width:324px;height:226px;border-radius:12px;overflow:hidden}
.category .label{position:absolute;left:50px;top:96px;width:236px;height:43px;background:var(--navy);color:var(--white);font-size:14px;display:flex;align-items:center;justify-content:center}
.category .label::before,.category .label::after{content:"";position:absolute;top:4px;bottom:4px;border-left:1px dashed var(--gold)}
.category .label::before{left:6px}.category .label::after{right:6px}
.linen{left:264px;top:595px;background:linear-gradient(135deg,#a69f92,#e2ddd4 50%,#bfb8ab)}
.canvas-cat{left:614px;top:595px;background:linear-gradient(135deg,#4a4656,#a29db0 60%,#7b7689)}
.sweet{left:264px;top:848px;background:linear-gradient(135deg,#5b7fd0,#2c48a6 55%,#1b2f7a)}
.jersey{left:614px;top:848px;background:linear-gradient(135deg,#f6b938,#f4a720 55%,#e8941a)}

/* products */
.shop-band{left:0;top:1114px;width:1200px;height:366px;background:var(--grey)}
.band-title{width:1200px;text-align:center;font-size:19px;font-weight:500;letter-spacing:.4px}
.product{width:159px;text-align:center}
.product .swatch{width:159px;height:159px}
.product .name{font-size:13px;margin-top:9px}
.product .price{font-size:13px;color:var(--gold)}
.btn{left:533px;top:1429px;width:135px;height:30px;border:1px solid var(--navy);font-size:12.5px;display:flex;align-items:center;justify-content:center}

/* markets */
.market{left:263px;width:675px;height:77px;border-bottom:1px solid var(--line)}
.market .city{position:absolute;left:0;top:0;font-size:19px;font-weight:600}
.market .addr{position:absolute;left:0;top:25px;font-size:18.5px;font-weight:400}
.market .date{position:absolute;right:8px;top:0;font-size:19px;font-weight:600}
.market .time{position:absolute;right:8px;top:25px;font-size:18.5px}

/* footer */
.site-footer{left:0;top:1882px;width:1200px;height:318px;background:radial-gradient(ellipse at 60% 40%,#1f3282,var(--navy-deep) 70%)}
.contact{left:263px;top:75px;color:var(--white);font-size:11.5px;font-weight:600;line-height:25.5px}
.contact li{list-style:none;display:flex;align-items:center}
.contact .ic{width:28px;display:inline-flex}
.social{left:866px;top:75px;display:flex;gap:9px}
.social span{width:25px;height:25px;border-radius:3px;background:var(--white)}
.legal{left:264px;top:2214px;font-size:13.5px;display:flex;gap:18px}
</style>
</head>
<body>

<header class="site-header abs">
  <div class="brand abs"><span class="brand-mark"></span><span class="brand-name">PALMTUCHE</span></div>
  <nav class="main-nav abs">
    <span class="active">WILLKOMMEN</span><span>SHOP</span><span>KONTAKT</span><span>TERMINE</span>
    <span><svg width="9" height="9" viewBox="0 0 10 10"><circle cx="5" cy="3" r="2.5" fill="#1d2a6e"/><path d="M0 10c0-4 10-4 10 0z" fill="#1d2a6e"/></svg> MEIN KONTO</span>
  </nav>
  <div class="nav-divider abs"></div>
  <svg class="cart abs" width="26" height="30" viewBox="0 0 26 30"><rect x="1" y="9" width="24" height="20" fill="none" stroke="#1d2a6e" stroke-width="1.6"/><path d="M7 12V6a6 6 0 0 1 12 0v6" fill="none" stroke="#1d2a6e" stroke-width="1.6"/></svg>
</header>

<div class="hero abs" role="img" aria-label="Foto: bunte gerollte Batikstoffe nebeneinander"></div>
<div class="hero-badge abs">
  <span class="stitch" style="left:16px"></span><span class="stitch" style="right:20px"></span>
  <div class="hero-title">PALMTUCHE</div>
  <div class="hero-tagline">Bunte Bahnen</div>
</div>

<section class="intro abs">
  <h1>ELEGANZ KOMMT NIE AUS DER MODE</h1>
  <div class="rule"></div>
  <p>Palmtuche ist schon seit 15 Jahren auf den Märkten unterwegs und verkauft seine hochwertigen Stoffe vor Ort.</p>
</section>

<div class="category linen abs" role="img" aria-label="Foto: Leinenstoff in Naturtönen"><span class="label">LINEN</span></div>
<div class="category canvas-cat abs" role="img" aria-label="Foto: grauer Strickstoff"><span class="label">CANVAS</span></div>
<div class="category sweet abs" role="img" aria-label="Foto: blauer Sweatstoff"><span class="label">SWEET</span></div>
<div class="category jersey abs" role="img" aria-label="Foto: gelber Jerseystoff"><span class="label">JERSEY</span></div>

<section class="shop-band abs">
  <svg class="abs" style="left:586px;top:16px" width="28" height="32" viewBox="0 0 28 32"><rect x="1.5" y="10" width="25" height="20" fill="none" stroke="#1d2a6e" stroke-width="1.6"/><path d="M8 13V7a6 6 0 0 1 12 0v6" fill="none" stroke="#1d2a6e" stroke-width="1.6"/></svg>
  <div class="band-title abs" style="top:59px">LUST AUF SOMMERSTOFFE?</div>
  <div class="product abs" style="left:262px;top:96px"><div class="swatch" style="background:#e6e2da" role="img" aria-label="Stoffmuster mit Bienen und Honiggläsern"></div><div class="name">Stoffname / Stoffart</div><div class="price">11,95 €/m</div></div>
  <div class="product abs" style="left:434px;top:96px"><div class="swatch" style="background:linear-gradient(135deg,#f2c9b8,#cde0e6 50%,#f0dca4)" role="img" aria-label="Stoffmuster mit bunten Blättern"></div><div class="name">Stoffname / Stoffart</div><div class="price">11,95 €/m</div></div>
  <div class="product abs" style="left:606px;top:96px"><div class="swatch" style="background:#22336d" role="img" aria-label="maritimes Stoffmuster mit Ankern und Muscheln"></div><div class="name">Stoffname / Stoffart</div><div class="price">11,95 €/m</div></div>
  <div class="product abs" style="left:779px;top:96px"><div class="swatch" style="background:#e7e1d6" role="img" aria-label="Stoffmuster mit Meerestieren"></div><div class="name">Stoffname / Stoffart</div><div class="price">11,95 €/m</div></div>
</section>
<div class="btn abs">JETZT EINKAUFEN</div>

<svg class="abs" style="left:583px;top:1516px" width="35" height="38" viewBox="0 0 35 38"><rect x="1.5" y="5" width="32" height="31" fill="none" stroke="#1d2a6e" stroke-width="2"/><rect x="1.5" y="5" width="32" height="6" fill="#1d2a6e"/><rect x="8" y="1" width="3" height="7" fill="#1d2a6e"/><rect x="24" y="1" width="3" height="7" fill="#1d2a6e"/><g fill="#1d2a6e"><rect x="7" y="15" width="3" height="3"/><rect x="13" y="15" width="3" height="3"/><rect x="19" y="15" width="3" height="3"/><rect x="25" y="15" width="3" height="3"/><rect x="7" y="21" width="3" height="3"/><rect x="13" y="21" width="3" height="3"/><rect x="19" y="21" width="3" height="3"/><rect x="25" y="21" width="3" height="3"/><rect x="7" y="27" width="3" height="3"/><rect x="13" y="27" width="3" height="3"/><rect x="19" y="27" width="3" height="3"/></g></svg>
<div class="band-title abs" style="top:1569px">TERMINE / MÄRKTE 2022</div>

<div class="market abs" style="top:1617px"><span class="city">HAMBURG-HARBURG</span><span class="addr">21073 Hamburg, Hamburgrer Rathausplatz</span><span class="date">SA. 03.09</span><span class="time">10.00-17.00</span></div>
<div class="market abs" style="top:1694px"><span class="city">PODSTAM</span><span class="addr">14467 Neuer Lustgarten, Lange Brücke / Breite Straße</span><span class="date">SO. 04.09</span><span class="time">10.00-17.00</span></div>
<div class="market abs" style="top:1771px"><span class="city">BERLIN</span><span class="addr">10249 Markthalle Prenzlauer Berg, Kastanienweg 14</span><span class="date">SO. 16.10</span><span class="time">10.00-17.00</span></div>

<footer class="site-footer abs" role="img" aria-label="Hintergrundfoto: dunkelblauer Samtstoff">
  <ul class="contact abs">
    <li><span class="ic"><svg width="11" height="11" viewBox="0 0 10 10"><circle cx="5" cy="3" r="2.5" fill="#fff"/><path d="M0 10c0-4 10-4 10 0z" fill="#fff"/></svg></span>Matthias Weller</li>
    <li><span class="ic"></span>PALMTUCHE - BUNTE BAHNEN</li>
    <li><span class="ic"><svg width="9" height="12" viewBox="0 0 9 12"><path d="M4.5 0a4.5 4.5 0 0 1 4.5 4.5C9 8 4.5 12 4.5 12S0 8 0 4.5A4.5 4.5 0 0 1 4.5 0z" fill="#fff"/><circle cx="4.5" cy="4.5" r="1.6" fill="#1d2a6e"/></svg></span>Lindenhofstraße 24</li>
    <li><span class="ic"></span>13407 Berlin</li>
    <li><span class="ic"><svg width="11" height="11" viewBox="0 0 12 12"><path d="M2 0l2.5 3-1.3 1.5a7 7 0 0 0 4.3 4.3L9 7.5 12 10l-2 2C4.5 12 0 7.5 0 2z" fill="#fff"/></svg></span>Tel.: 0176/48219037</li>
    <li><span class="ic"><svg width="11" height="8" viewBox="0 0 12 8"><rect width="12" height="8" fill="#fff"/><path d="M0 0l6 5 6-5" fill="none" stroke="#1d2a6e" stroke-width="1"/></svg></span>palmtuche.stoffe@mail.de</li>
  </ul>
  <div class="social abs"><span></span><span></span></div>
</footer>

<div class="legal abs"><span>Impressum</span><span>|</span><span>Datenschutz</span></div>

</body>
</html>
```